WTF!!! We need a modern professional website for a business litigation law firm.

We need a modern, clean, professional and uncomplicated website for a new business trial and litigation law firm called "Hallorand Trial Firm PLLC". Website must be mobile optimized for iPad and smartphone. The law firm specializes in counseling and representing large corporations, small businesses and entrepreneurs in and out of the courtroom. Lawyers in the firm serve as Florida counsel and trial counsel to organizations facing claims involving product liability, premises liability, professional liability, vehicle and transportation liability, warranty claims, construction defects and delay claims, complex business disputes, commercial litigation and bid disputes in State and Federal Courts. The website is mainly to provide information about the firm, and should include sections describing the firm, identifying the Industries Served and Areas of Practice ," a separate page identifying the "Professionals", a separate page for "Resources & Advisories," and a traveling "Connect With Us" button a site visitor can click on that will launch an email to the Firm's general email account. The website should allow us to easily modify the content on these pages, and let us add/modify links to external information sources. We will not sell anything or take payments through the website. We do need to be able to easily upload and update photographs of attorneys and add new attorneys names/email hyperlinks as the firm grows. We would like to add developments in the law or success stories easily and quickly, such as through a blog page. On the "Connect With Us" page the website should have hyperlinks to email the Firm, and there should be hyperlinks to email each professional on the "Professionals" page. The website should be viewable on mobile devices without distortion. The law firm focuses on trial work and should have some imagery associated with courtrooms, but the overall theme of the site should be modern, clean, and communicate sophistication and strength. The website should be made in Wordpress. We have uploaded logo files for Hallorand Trial Firm.

Target Market(s)

Corporations and companies that are looking for legal representation. Other attorneys/legal industry.

Industry/Entity Type

Legal Industry

Coding

Coded - Design and coding required

Number of Pages Required

1 page

Font styles to use
Sans Serif

Requirements
Must have
• Simple, clean, sophisticated, modern website that includes the logo, watermark of logo, and the elements described above.
Nice to have
• Pictures of city scape, buildings, courtroom, team members.

```html
<!DOCTYPE html>
<html lang="en">
<head>
<meta charset="utf-8">
<title>Hallorand Trial Firm PLLC</title>
<link href="https://fonts.googleapis.com/css2?family=Poppins:wght@700;800&family=Roboto:wght@400;500;700;900&display=swap" rel="stylesheet">
<style>
:root{
  --red:#d9382b;
  --red-dark:#a3231a;
  --ink:#1f1f1f;
  --base:#242424;
  --band:#2e2e2e;
  --card:#3b3b3b;
  --text:#ffffff;
  --muted:#bdbdbd;
  --field:#2a2a2a;
}
*{box-sizing:border-box;margin:0;padding:0}
html,body{width:1200px;height:3750px;overflow:hidden}
body{position:relative;background:var(--base);color:var(--text);font-family:"Roboto",Arial,sans-serif}
.abs{position:absolute}
.center{text-align:center}
.btn{position:absolute;background:var(--red);color:#fff;font:700 11px "Roboto",sans-serif;letter-spacing:.5px;display:flex;align-items:center;justify-content:center;text-transform:uppercase}
.read-more{color:var(--red);font:700 10.5px "Roboto",sans-serif;letter-spacing:.5px;display:inline-flex;align-items:center;gap:6px}
.section-title{position:absolute;left:0;width:1200px;text-align:center;font:700 30px "Roboto",sans-serif;text-transform:uppercase;letter-spacing:.2px}

/* hero */
.hero-photo{position:absolute;left:0;top:0;width:1200px;height:600px;
  background:
    radial-gradient(ellipse 260px 300px at 600px 330px,rgba(30,30,34,.85),rgba(30,30,34,0) 70%),
    radial-gradient(ellipse 140px 260px at 340px 360px,rgba(35,35,38,.8),rgba(35,35,38,0) 70%),
    radial-gradient(ellipse 140px 260px at 185px 380px,rgba(30,30,30,.8),rgba(30,30,30,0) 70%),
    radial-gradient(ellipse 140px 260px at 800px 360px,rgba(30,30,30,.75),rgba(30,30,30,0) 70%),
    radial-gradient(ellipse 140px 260px at 1000px 380px,rgba(25,25,25,.8),rgba(25,25,25,0) 70%),
    linear-gradient(180deg,#4a5260 0%,#5f6470 18%,#8a7458 32%,#5a4a3c 45%,#2f2c2a 70%,#252525 100%)}
.brand{position:absolute;left:121px;top:50px;width:110px;text-align:center;font:700 17px "Roboto",sans-serif;line-height:1;color:#fff}
.brand small{display:block;font-size:8px;letter-spacing:2px;margin-top:3px}
.nav{position:absolute;top:36px;font:500 11px "Roboto",sans-serif;letter-spacing:.3px;color:#fff}
.nav.active{color:var(--red)}
.call{position:absolute;left:780px;top:28px;display:flex;gap:10px;align-items:center}
.call-label{font:400 10px "Roboto",sans-serif}
.call-num{font:700 16px "Roboto",sans-serif}
.hero-title{position:absolute;left:0;width:1200px;text-align:center;font-family:"Poppins",sans-serif;font-weight:800}
.hero-tag{position:absolute;left:0;top:528px;width:1200px;text-align:center;font:700 15px "Roboto",sans-serif;letter-spacing:2px}

/* connect bar */
.connect-bar{position:absolute;left:121px;top:593px;width:956px;height:81px;background:#3a3a3a;border:2px solid var(--red-dark)}
.connect-field{position:absolute;top:22px;height:34px;background:var(--field);font:400 11px "Roboto",sans-serif;color:#ddd;padding:11px 0 0 20px}

/* practice grid */
.card-title{position:absolute;width:220px;text-align:center;font:500 14.5px "Roboto",sans-serif;line-height:18px;text-transform:uppercase}
.card-more{position:absolute;width:220px;text-align:center}

/* resources */
.media{position:absolute}
.res-date{font:400 10.5px "Roboto",sans-serif;color:#cfcfcf}
.res-title{font:700 12.5px "Roboto",sans-serif;line-height:17px;text-transform:uppercase}

/* footer */
.foot-h{position:absolute;top:3536px;font:700 14px "Roboto",sans-serif;letter-spacing:.6px}
.foot-link{position:absolute;font:400 9.5px "Roboto",sans-serif;color:#ddd}
.foot-icon{position:absolute;width:20px;height:20px;border-radius:50%;background:#3a3a3a;display:flex;align-items:center;justify-content:center}
</style>
</head>
<body>

<!-- HERO -->
<div class="hero-photo" role="img" aria-label="Night city skyline with five attorneys standing arms crossed"></div>
<div class="brand">HALLORAND<small>TRIAL FIRM</small></div>
<div class="nav active" style="left:301px">HOME</div>
<div class="nav" style="left:360px">AREAS OF PRACTICE</div>
<div class="nav" style="left:497px">PROFESSIONALS</div>
<div class="nav" style="left:612px">RESOURCES &amp; ADVISORIES</div>
<div class="call">
  <svg width="30" height="30" viewBox="0 0 30 30"><circle cx="15" cy="15" r="15" fill="#111"/><rect x="10" y="7" width="10" height="16" rx="2" fill="none" stroke="#d9382b" stroke-width="2"/></svg>
  <div><div class="call-label">CALL US TODAY:</div><div class="call-num">954-555-0142</div></div>
</div>
<div class="btn" style="left:946px;top:26px;width:131px;height:32px">Connect with us</div>

<div class="hero-title" style="top:368px;font-size:90px;line-height:96px;letter-spacing:1px">HALLORAND</div>
<div class="hero-title" style="top:464px;font-size:42px;line-height:50px;font-weight:700;letter-spacing:4px">TRIAL FIRM PLLC</div>
<div class="hero-tag">A NEW BUSINESS TRIAL AND LITIGATION LAW FIRM</div>

<div class="connect-bar">
  <svg class="abs" style="left:-2px;top:-2px" width="206" height="81" viewBox="0 0 206 81"><polygon points="0,0 206,0 170,81 0,81" fill="#d9382b"/>
    <polygon points="20,46 58,26 44,58 38,48" fill="#fff"/></svg>
  <div class="abs" style="left:70px;top:20px;font:700 17px Roboto,sans-serif;line-height:21px">CONNECT<br>WITH US</div>
  <div class="connect-field" style="left:196px;width:150px;clip-path:polygon(0 0,100% 0,90% 100%,0 100%)">Name</div>
  <div class="connect-field" style="left:350px;width:150px;clip-path:polygon(10% 0,100% 0,90% 100%,0 100%)">Email</div>
  <div class="connect-field" style="left:503px;width:150px;clip-path:polygon(10% 0,100% 0,90% 100%,0 100%)">Phone</div>
  <div class="connect-field" style="left:656px;width:150px;clip-path:polygon(10% 0,100% 0,100% 100%,0 100%)">Subject
    <svg class="abs" style="right:8px;top:15px" width="8" height="5"><polyline points="0,0 4,4 8,0" fill="none" stroke="#ddd"/></svg></div>
  <div class="btn" style="left:815px;top:22px;width:126px;height:34px">Let's connect</div>
</div>

<!-- PRACTICE AREAS -->
<div class="section-title" style="top:716px">Industries served and areas of practice</div>
<div class="abs center" style="left:0;top:757px;width:1200px;font-size:10.5px;color:#ccc">Lorem ipsum dolor sit amet, consectetur adipiscing elit. Ut porta feugiat dolor, vel dictum eros. Cras porta diam sed est tincidunt.</div>

<svg class="abs" style="left:0;top:799px" width="1200" height="441" viewBox="0 0 1200 441">
  <g fill="#3b3b3b">
    <polygon points="121,0 367,0 345,216 121,216"/>
    <polygon points="375,0 606,0 584,216 353,216"/>
    <polygon points="614,0 845,0 823,216 592,216"/>
    <polygon points="853,0 1077,0 1077,216 831,216"/>
    <polygon points="121,226 367,226 345,440 121,440"/>
    <polygon points="375,226 606,226 584,440 353,440"/>
    <polygon points="614,226 845,226 823,440 592,440"/>
    <polygon points="853,226 1077,226 1077,440 831,440"/>
  </g>
  <g fill="#111">
    <circle cx="240" cy="69" r="43"/><circle cx="476" cy="69" r="43"/><circle cx="718" cy="69" r="43"/><circle cx="962" cy="69" r="43"/>
    <circle cx="240" cy="293" r="43"/><circle cx="476" cy="293" r="43"/><circle cx="718" cy="293" r="43"/><circle cx="962" cy="293" r="43"/>
  </g>
  <g fill="#d9382b" stroke="none">
    <rect x="222" y="62" width="36" height="24" rx="3"/><circle cx="240" cy="52" r="7"/>
    <circle cx="476" cy="69" r="20" fill="none" stroke="#d9382b" stroke-width="4"/><text x="476" y="77" font-family="Roboto" font-weight="900" font-size="22" text-anchor="middle">$</text>
    <path d="M703 54 L718 48 L733 54 L733 70 Q733 84 718 90 Q703 84 703 70Z"/>
    <path d="M947 52 L962 46 L977 52 L977 70 Q977 84 962 90 Q947 84 947 70Z" fill="none" stroke="#d9382b" stroke-width="4"/><polyline points="954,68 960,74 970,62" fill="none" stroke="#d9382b" stroke-width="3"/>
    <circle cx="238" cy="291" r="16"/><circle cx="252" cy="306" r="9" fill="#111" stroke="#d9382b" stroke-width="3"/>
    <rect x="474" y="272" width="4" height="38"/><rect x="456" y="278" width="40" height="3"/><path d="M452 296 L466 296 Q459 306 452 296Z"/><path d="M486 296 L500 296 Q493 306 486 296Z"/><rect x="464" y="310" width="24" height="4"/>
    <circle cx="718" cy="293" r="22" fill="none" stroke="#d9382b" stroke-width="4"/><circle cx="718" cy="293" r="12" fill="none" stroke="#d9382b" stroke-width="4"/><circle cx="718" cy="293" r="4"/>
    <path d="M942 300 L948 284 L976 284 L982 300 L982 312 L942 312Z"/><circle cx="962" cy="276" r="6"/>
  </g>
</svg>
<div class="card-title" style="left:130px;top:920px">Product<br>liability</div>
<div class="card-title" style="left:366px;top:920px">Premises<br>liability</div>
<div class="card-title" style="left:608px;top:920px">Professional<br>liability</div>
<div class="card-title" style="left:852px;top:920px">Warranty<br>claims</div>
<div class="card-title" style="left:130px;top:1145px">Construction<br>defects &amp; delay<br>claims</div>
<div class="card-title" style="left:366px;top:1145px">Commercial litigation<br>&amp; bid disputes in state<br>&amp; federal courts</div>
<div class="card-title" style="left:608px;top:1145px">Complex<br>business disputes</div>
<div class="card-title" style="left:852px;top:1145px">Vehicle &amp;<br>transportation<br>liability</div>
<div class="card-more" style="left:130px;top:980px"><span class="read-more">READ MORE <svg width="16" height="6"><path d="M0 3H15M12 0L15 3L12 6" stroke="#d9382b" fill="none"/></svg></span></div>
<div class="card-more" style="left:366px;top:980px"><span class="read-more">READ MORE <svg width="16" height="6"><path d="M0 3H15M12 0L15 3L12 6" stroke="#d9382b" fill="none"/></svg></span></div>
<div class="card-more" style="left:608px;top:980px"><span class="read-more">READ MORE <svg width="16" height="6"><path d="M0 3H15M12 0L15 3L12 6" stroke="#d9382b" fill="none"/></svg></span></div>
<div class="card-more" style="left:852px;top:980px"><span class="read-more">READ MORE <svg width="16" height="6"><path d="M0 3H15M12 0L15 3L12 6" stroke="#d9382b" fill="none"/></svg></span></div>
<div class="card-more" style="left:130px;top:1205px"><span class="read-more">READ MORE <svg width="16" height="6"><path d="M0 3H15M12 0L15 3L12 6" stroke="#d9382b" fill="none"/></svg></span></div>
<div class="card-more" style="left:366px;top:1205px"><span class="read-more">READ MORE <svg width="16" height="6"><path d="M0 3H15M12 0L15 3L12 6" stroke="#d9382b" fill="none"/></svg></span></div>
<div class="card-more" style="left:608px;top:1205px"><span class="read-more">READ MORE <svg width="16" height="6"><path d="M0 3H15M12 0L15 3L12 6" stroke="#d9382b" fill="none"/></svg></span></div>
<div class="card-more" style="left:852px;top:1205px"><span class="read-more">READ MORE <svg width="16" height="6"><path d="M0 3H15M12 0L15 3L12 6" stroke="#d9382b" fill="none"/></svg></span></div>

<div class="btn" style="left:523px;top:1271px;width:154px;height:37px">View all services</div>

<div class="abs" style="left:0;top:1318px;width:1200px;height:65px;overflow:hidden;white-space:nowrap;font:900 80px/78px 'Roboto',sans-serif;color:#3a3a3a;letter-spacing:2px;text-align:center">HALLORAND TRIAL FIRM PLLC</div>

<!-- RESOURCES -->
<div class="abs" style="left:0;top:1383px;width:1200px;height:547px;background:var(--band)"></div>
<div class="section-title" style="top:1426px">Latest resources &amp; advisories</div>
<div class="media" style="left:121px;top:1485px;width:498px;height:213px;background:linear-gradient(180deg,#c4bfb2 0%,#a89a82 35%,#8a6e4e 60%,#6b3a2c 78%,#3f3a2c 100%)" role="img" aria-label="Classical columned courthouse building"></div>
<div class="abs" style="left:121px;top:1713px;width:430px">
  <div class="res-date">February 28, 2024</div>
  <div class="res-title" style="margin-top:6px;font-size:14px">Pellentesque feugiat, purus vitae maximus finibus.</div>
  <div style="font-size:10.5px;color:#c9c9c9;line-height:15px;margin-top:4px">Lorem ipsum dolor sit amet, consectetur adipiscing elit. Ut porta feugiat dolor, vel dictum eros. Cras porta diam sed est tincidunt.</div>
  <div class="read-more" style="margin-top:10px">READ MORE <svg width="16" height="6"><path d="M0 3H15M12 0L15 3L12 6" stroke="#d9382b" fill="none"/></svg></div>
</div>

<div class="media" style="left:671px;top:1485px;width:166px;height:102px;background:linear-gradient(160deg,#e0dbd2 0%,#b9b0a4 50%,#5e554c 100%)" role="img" aria-label="Gavel resting on open law books"></div>
<div class="media" style="left:671px;top:1597px;width:166px;height:101px;background:linear-gradient(160deg,#eef1f3 0%,#9aa3ab 50%,#3e4650 100%)" role="img" aria-label="Handshake over desk with gavel"></div>
<div class="media" style="left:671px;top:1709px;width:166px;height:101px;background:linear-gradient(160deg,#f2f2f2 0%,#c9c4bd 55%,#7a5a44 100%)" role="img" aria-label="Scales of justice and gavel"></div>

<div class="abs" style="left:855px;top:1493px;width:225px">
  <div class="res-date">February 28, 2024</div>
  <div class="res-title" style="margin-top:8px">There are many variations of passages of lorem ipsum.</div>
  <div class="read-more" style="margin-top:9px">READ MORE <svg width="16" height="6"><path d="M0 3H15M12 0L15 3L12 6" stroke="#d9382b" fill="none"/></svg></div>
</div>
<div class="abs" style="left:855px;top:1606px;width:225px">
  <div class="res-date">February 28, 2024</div>
  <div class="res-title" style="margin-top:8px">If you are going to use a passage of lorem ipsum.</div>
  <div class="read-more" style="margin-top:9px">READ MORE <svg width="16" height="6"><path d="M0 3H15M12 0L15 3L12 6" stroke="#d9382b" fill="none"/></svg></div>
</div>
<div class="abs" style="left:855px;top:1719px;width:225px">
  <div class="res-date">February 28, 2024</div>
  <div class="res-title" style="margin-top:8px">All the lorem ipsum generators on the internet tend.</div>
  <div class="read-more" style="margin-top:9px">READ MORE <svg width="16" height="6"><path d="M0 3H15M12 0L15 3L12 6" stroke="#d9382b" fill="none"/></svg></div>
</div>
<div class="btn" style="left:523px;top:1840px;width:154px;height:38px">View all resources</div>

<!-- ABOUT -->
<div class="abs" style="left:0;top:1930px;width:1200px;height:432px;background:
  radial-gradient(ellipse 420px 160px at 600px 220px,rgba(40,40,40,.55),rgba(40,40,40,0) 75%),
  radial-gradient(ellipse 260px 120px at 450px 60px,rgba(150,150,150,.45),rgba(150,150,150,0) 75%),
  radial-gradient(ellipse 300px 200px at 1050px 150px,rgba(20,20,20,.5),rgba(20,20,20,0) 75%),
  radial-gradient(ellipse 300px 200px at 120px 180px,rgba(25,25,25,.5),rgba(25,25,25,0) 75%),
  linear-gradient(180deg,#747474 0%,#5c5c5c 30%,#444 60%,#2e2e2e 100%)" role="img" aria-label="Black and white courtroom with judge and attorneys"></div>
<div class="section-title" style="top:2090px">About Hallorand trial firm PLLC</div>
<div class="abs center" style="left:345px;top:2136px;width:510px;font-size:11px;line-height:17.5px;color:#eee">Lorem ipsum dolor sit amet, consectetur adipiscing elit. Ut porta feugiat dolor, vel dictum eros. Cras porta diam sed est tincidunt, at placerat mi vestibulum. Duis pellentesque ut nisi sit amet auctor. Nullam dignissim dolor vel lectus dictum lacinia ut nec velit. Phasellus sollicitudin risus nec tincidunt egestas.</div>
<div class="btn" style="left:523px;top:2232px;width:154px;height:36px">Learn more</div>

<!-- REVIEWS -->
<div class="abs" style="left:0;top:2362px;width:1200px;height:524px;background:var(--band)"></div>
<div class="abs" style="left:0;top:2665px;width:1200px;height:221px;background:
  radial-gradient(ellipse 500px 90px at 600px 60px,rgba(46,46,46,.9),rgba(46,46,46,0) 80%),
  linear-gradient(180deg,#2e2e2e 0%,#4a4d53 30%,#6a6e75 55%,#3d4046 100%)" role="img" aria-label="Curved colonnade of a government building"></div>
<div class="section-title" style="top:2406px">Real customer, real reviews.</div>
<svg class="abs" style="left:556px;top:2476px" width="86" height="86"><circle cx="43" cy="43" r="41" fill="#6d7581" stroke="#d9382b" stroke-width="3"/></svg>
<div class="abs center" style="left:0;top:2580px;width:1200px;font:500 13px Roboto,sans-serif">MARTIN REYES</div>
<div class="abs center" style="left:0;top:2596px;width:1200px;color:var(--red);font-size:15px;letter-spacing:1px">★★★★★</div>
<div class="abs center" style="left:360px;top:2627px;width:480px;font-size:10.5px;line-height:18px;color:#cfcfcf">"Lorem ipsum dolor sit amet, consectetur adipiscing elit. Ut porta feugiat dolor, vel dictum eros. Cras porta diam sed est tincidunt, at placerat mi vestibulum. Duis pellentesque ut nisi sit amet auctor.  Nullam dignissim dolor vel lectus dictum lacinia ut nec velit."</div>
<svg class="abs" style="left:232px;top:2547px" width="33" height="33"><circle cx="16.5" cy="16.5" r="16" fill="#c9c9c9"/><polyline points="19,10 13,16.5 19,23" fill="none" stroke="#333" stroke-width="2.5"/></svg>
<svg class="abs" style="left:935px;top:2547px" width="33" height="33"><circle cx="16.5" cy="16.5" r="16" fill="#c9c9c9"/><polyline points="14,10 20,16.5 14,23" fill="none" stroke="#333" stroke-width="2.5"/></svg>

<!-- MAP -->
<div class="abs" style="left:0;top:2886px;width:1200px;height:518px;background:
  radial-gradient(ellipse 90px 130px at 780px 120px,rgba(150,200,160,.7),rgba(150,200,160,0) 80%),
  radial-gradient(ellipse 60px 320px at 515px 250px,rgba(120,150,200,.45),rgba(120,150,200,0) 85%),
  radial-gradient(ellipse 200px 120px at 560px 180px,rgba(255,255,255,.5),rgba(255,255,255,0) 80%),
  linear-gradient(135deg,#dfe2e6 0%,#cfd4da 50%,#c3c9d1 100%)" role="img" aria-label="Street map showing the firm office location"></div>

<!-- CONTACT CTA -->
<div class="abs" style="left:121px;top:3308px;width:956px;height:192px;background:linear-gradient(90deg,#5e0f0a 0%,#b52a20 14%,#d9382b 30%,#d9382b 70%,#b52a20 86%,#5e0f0a 100%)" role="img" aria-label="Red toned courthouse columns"></div>
<div class="abs center" style="left:0;top:3338px;width:1200px;font:700 30px Roboto,sans-serif">CONTACT US TODAY!</div>
<div class="abs center" style="left:430px;top:3384px;width:340px;font-size:10.5px;line-height:15px">Lorem ipsum dolor sit amet, consectetur adipiscing elit. Nunc egestas efficitur interdum. Aenean mattis mauris lorem.</div>
<div class="btn" style="left:523px;top:3426px;width:154px;height:36px;background:#fff;color:#222;font-weight:500">Connect with us</div>

<!-- FOOTER -->
<div class="abs" style="left:0;top:3500px;width:1200px;height:250px;background:var(--ink)"></div>
<div class="foot-h" style="left:121px">NAVIGATIONS</div>
<div class="foot-link" style="left:121px;top:3563px">Home</div>
<div class="foot-link" style="left:121px;top:3586px">Areas of Practice</div>
<div class="foot-link" style="left:121px;top:3608px">Professionals</div>
<div class="foot-link" style="left:121px;top:3631px">Resources &amp; Advisories</div>
<div class="foot-link" style="left:121px;top:3654px">Contact Us</div>

<div class="foot-h" style="left:284px">CONTACT US</div>
<div class="foot-icon" style="left:286px;top:3561px"><svg width="10" height="12"><path d="M5 12 L1 6 A4 4 0 1 1 9 6Z" fill="#fff"/><circle cx="5" cy="4.5" r="1.5" fill="#3a3a3a"/></svg></div>
<div class="foot-link" style="left:314px;top:3563px;line-height:15px">2400 Harbor Ave., Suite 310,<br>Fort Lauderdale, FL 33301</div>
<div class="foot-icon" style="left:286px;top:3608px"><svg width="10" height="10"><path d="M1 1 L4 1 L5 3.5 L3.5 4.5 Q5 6.5 5.5 6.5 L6.5 5 L9 6 L9 9 Q3 9.5 1 1Z" fill="#fff"/></svg></div>
<div class="foot-link" style="left:314px;top:3613px">(954) 555-0198</div>
<div class="foot-icon" style="left:286px;top:3640px"><svg width="11" height="8"><rect x="0.5" y="0.5" width="10" height="7" fill="none" stroke="#fff"/><polyline points="0.5,0.5 5.5,4.5 10.5,0.5" fill="none" stroke="#fff"/></svg></div>
<div class="foot-link" style="left:314px;top:3645px;color:var(--red)">contact@hallorandlaw.example</div>

<div class="abs center" style="left:480px;top:3608px;width:240px;font:700 29px/30px Roboto,sans-serif">HALLORAND<br><span style="font-size:15px;letter-spacing:3px;line-height:18px">TRIAL FIRM</span></div>

<div class="foot-h" style="left:751px">FOLLOW US</div>
<div class="foot-icon" style="left:753px;top:3562px"><svg width="6" height="6"><circle cx="3" cy="3" r="3" fill="#fff"/></svg></div>
<div class="foot-link" style="left:782px;top:3566px">Friendbook</div>
<div class="foot-icon" style="left:753px;top:3596px"><svg width="6" height="6"><circle cx="3" cy="3" r="3" fill="#fff"/></svg></div>
<div class="foot-link" style="left:782px;top:3600px">Linkfolio</div>
<div class="foot-icon" style="left:753px;top:3629px"><svg width="6" height="6"><circle cx="3" cy="3" r="3" fill="#fff"/></svg></div>
<div class="foot-link" style="left:782px;top:3633px">Chirper</div>

<div class="foot-h" style="left:887px">SUBSCRIBE NEWSLETTER</div>
<div class="foot-link" style="left:887px;top:3563px;width:170px;line-height:14px">Enter your email below and get latest updates right int your inbox.</div>
<div class="abs" style="left:887px;top:3609px;width:190px;height:32px;background:#3a3a3a"></div>
<svg class="abs" style="left:897px;top:3621px" width="11" height="8"><rect x="0.5" y="0.5" width="10" height="7" fill="none" stroke="#aaa"/><polyline points="0.5,0.5 5.5,4.5 10.5,0.5" fill="none" stroke="#aaa"/></svg>
<div class="btn" style="left:1002px;top:3609px;width:75px;height:32px">Subscribe</div>

<div class="abs" style="left:121px;top:3688px;width:956px;height:1px;background:#3a3a3a"></div>
<div class="abs center" style="left:0;top:3708px;width:1200px;font-size:8.5px;color:#ddd">Site Map &nbsp;|&nbsp; Privacy Policy &nbsp;|&nbsp; Terms &nbsp;|&nbsp; Copyright © 2025 Hallorand Trial Firm &nbsp;|&nbsp; All Rights Reserved.</div>

</body>
</html>
```